Employee Benefits Flyer for Recruiting

We are a Steel Product Supplier and Manufacturer in Toledo Ohio.

We would like to create an "attention getting", one-page handout to give prospective employees (both production and administrative) that illustrates all the benefits we offer as a company. An editable document would be preferable as we add more or change existing benefits in the future. Current benefits include:

Individual and Family Medical Insurance
Dental Insurance
Vision Insurance
Short Term Disability Insurance
Critical Illness and Accident Insurance
No Cost Life Insurance Policy
Education Cost Reimbursement
401K with Company Match
Profit Sharing
Attendance and Performance Bonuses
No Cost Legal Assistance
No Cost Counseling Services
No Cost Tobacco Cessation Coaching
No Cost College Planning Assistance
No Cost Work-Life Services
No Cost Employee Discounts
No Cost Legal Consultation
No Cost Financial Consultation
No Cost ID Theft Assistance
No Cost Tax Consultation Assistance
Up to 17 Days of Paid Time Off

Target Market(s)

Potential Employees

Industry/Entity Type

Industrial Manufacturing

Requirements
Must have
• Nicely laid out illustrations / engaging content

```html
<!DOCTYPE html>
<html lang="en">
<head>
<meta charset="utf-8">
<title>Ironvale Steel Works – We Are Hiring</title>
<link rel="stylesheet" href="https://fonts.googleapis.com/css2?family=Russo+One&family=Kanit:wght@500&family=Montserrat:wght@500;600;700;800&display=swap">
<style>
  :root {
    --navy: #0d2350;
    --navy-deep: #081634;
    --orange: #f26a12;
    --orange-bright: #ff7a1a;
    --blue: #1a52c8;
    --white: #ffffff;
    --ink: #1a1f2b;
  }
  * { box-sizing: border-box; margin: 0; padding: 0; }
  html, body { width: 684px; height: 1200px; overflow: hidden; background: var(--navy-deep); }
  .flyer {
    position: relative; width: 684px; height: 1200px; overflow: hidden;
    background: linear-gradient(180deg, var(--navy-deep) 0%, var(--navy) 45%, #10285a 100%);
    font-family: "Montserrat", sans-serif;
  }
  .hero-photo {
    position: absolute; left: 0; top: 0; width: 684px; height: 530px;
    background:
      linear-gradient(90deg, var(--navy-deep) 0%, rgba(8,22,52,.85) 30%, rgba(8,22,52,0) 62%),
      linear-gradient(180deg, rgba(8,22,52,0) 70%, var(--navy) 100%),
      radial-gradient(circle at 57% 32%, #e8853a 0%, #8a4a2a 8%, rgba(60,70,100,0) 22%),
      radial-gradient(ellipse at 88% 28%, #2f7f86 0%, #1d5560 30%, rgba(30,60,90,0) 55%),
      linear-gradient(135deg, #3b4a6e 0%, #2a3756 50%, #1a2644 100%);
  }
  .brand {
    position: absolute; left: 36px; top: 176px;
    display: flex; align-items: center; gap: 10px;
  }
  .brand-dot { width: 22px; height: 22px; border-radius: 50%; background: var(--blue); }
  .brand-name { font-weight: 800; font-size: 20px; color: var(--white); letter-spacing: .5px; }
  .headline-we {
    position: absolute; left: 36px; top: 246px;
    font-weight: 800; font-size: 66px; line-height: 1;
    color: var(--orange);
  }
  .headline-hiring {
    position: absolute; left: 32px; top: 340px;
    font-family: "Russo One", sans-serif; font-size: 78px; line-height: 1; letter-spacing: -1px;
    transform: skewX(-10deg); transform-origin: left bottom;
    background: linear-gradient(180deg, #ffffff 0%, #e3e6ea 40%, #8e949d 55%, #d9dce1 75%, #ffffff 100%);
    -webkit-background-clip: text; background-clip: text; color: transparent;
  }
  .roles {
    position: absolute; left: 30px; top: 442px;
    font-family: "Russo One", sans-serif; font-size: 18px; letter-spacing: .6px;
    color: var(--orange);
  }
  .tagline {
    position: absolute; left: 34px; top: 484px;
    font-family: "Kanit", sans-serif; font-weight: 500; font-size: 18.5px; color: var(--white);
  }
  .tagline .place { color: var(--orange); }
  .photo-strip { position: absolute; left: 0; top: 530px; width: 684px; height: 175px; }
  .benefits-banner {
    position: absolute; left: 78px; top: 727px; width: 520px; height: 44px; z-index: 2;
    background: var(--orange);
    clip-path: polygon(0 0, 100% 0, 95% 100%, 5% 100%);
    display: flex; align-items: center; justify-content: center;
    font-weight: 800; font-style: italic; font-size: 19.5px;
    color: var(--navy-deep); letter-spacing: .3px;
  }
  .benefits-panel {
    position: absolute; left: 31px; top: 752px; width: 623px; height: 278px;
    border: 3px solid #d6d9de;
    background:
      repeating-linear-gradient(90deg, rgba(255,255,255,.18) 0 1px, rgba(0,0,0,.03) 1px 3px),
      linear-gradient(90deg, #9ea4ad 0%, #e9ebee 25%, #c3c8cf 50%, #f1f2f4 72%, #a4aab3 100%);
    display: grid; grid-template-columns: 200px 204px 190px; column-gap: 4px;
    padding: 36px 10px 12px 12px;
  }
  .benefit-list { list-style: none; display: flex; flex-direction: column; gap: 12px; }
  .benefit-list li {
    position: relative; padding-left: 16px;
    font-size: 12.2px; font-weight: 500; line-height: 1.12; color: var(--ink);
  }
  .benefit-list li::before {
    content: ""; position: absolute; left: 0; top: 3px; width: 8px; height: 8px; border-radius: 50%;
    background: radial-gradient(circle at 35% 35%, #d8dbe0, #5d636c);
  }
  .footer-band {
    position: absolute; left: 0; top: 1085px; width: 684px; height: 115px;
    background: linear-gradient(90deg, #cfd3d9 0%, #ffffff 35%, #b7bcc4 70%, #e4e6ea 100%);
  }
  .footer-graphic { position: absolute; left: 0; top: 1050px; width: 684px; height: 150px; }
  .contact { position: absolute; left: 22px; top: 1098px; }
  .contact-row { display: flex; align-items: center; gap: 10px; color: var(--ink); }
  .contact-phone { font-size: 27px; font-weight: 700; letter-spacing: .5px; }
  .contact-web { font-size: 17px; font-weight: 700; margin-top: 4px; }
  .apply { position: absolute; right: 30px; top: 1080px; text-align: right; color: var(--white); }
  .apply-title {
    font-weight: 800; font-style: italic; font-size: 30px;
    color: var(--orange-bright); letter-spacing: 1px; line-height: 1.1;
  }
  .apply-note { font-size: 13px; font-weight: 500; letter-spacing: .5px; margin-top: 2px; }
  .apply-email { display: flex; align-items: center; justify-content: flex-end; gap: 8px; font-size: 18px; font-weight: 600; margin-top: 1px; }
</style>
</head>
<body>
<main class="flyer">
  <div class="hero-photo" role="img" aria-label="Worker in teal jacket and blue gloves grinding a large steel pipe with sparks flying"></div>

  <div class="brand">
    <span class="brand-dot"></span>
    <span class="brand-name">IRONVALE STEEL WORKS</span>
  </div>

  <h1>
    <span class="headline-we">We Are</span>
    <span class="headline-hiring">HIRING!</span>
  </h1>
  <p class="roles">PRODUCTION AND ADMINISTRATIVE</p>
  <p class="tagline">We are a Steel Product Supplier and Manufacturer in <span class="place">Toledo, Ohio</span></p>

  <svg class="photo-strip" viewBox="0 530 684 175" width="684" height="175">
    <defs>
      <linearGradient id="silver" x1="0" y1="0" x2="0" y2="1">
        <stop offset="0" stop-color="#ffffff"/><stop offset=".45" stop-color="#b9bec6"/>
        <stop offset=".55" stop-color="#8d939c"/><stop offset="1" stop-color="#eceef1"/>
      </linearGradient>
      <linearGradient id="weld" x1="0" y1="0" x2="1" y2="1">
        <stop offset="0" stop-color="#3a2a22"/><stop offset=".45" stop-color="#d98a2b"/><stop offset="1" stop-color="#2a4fb0"/>
      </linearGradient>
      <linearGradient id="building" x1="0" y1="0" x2="0" y2="1">
        <stop offset="0" stop-color="#b9c2cc"/><stop offset=".5" stop-color="#2f6fb5"/><stop offset="1" stop-color="#4b6b34"/>
      </linearGradient>
      <linearGradient id="coils" x1="0" y1="0" x2="1" y2="0">
        <stop offset="0" stop-color="#5d6f86"/><stop offset=".5" stop-color="#9fb0c2"/><stop offset="1" stop-color="#4a5a66"/>
      </linearGradient>
    </defs>
    <rect x="220" y="598" width="42" height="34" fill="url(#silver)"/>
    <rect x="436" y="598" width="42" height="34" fill="url(#silver)"/>
    <polygon points="43,534 240,534 222,697 25,697" fill="url(#silver)"/>
    <polygon points="265,534 458,534 440,697 247,697" fill="url(#silver)"/>
    <polygon points="480,534 668,534 650,697 462,697" fill="url(#silver)"/>
    <g role="img" aria-label="Welder in protective helmet and gloves welding with bright blue arc">
      <polygon points="48,539 233,539 217,692 31,692" fill="url(#weld)"/>
    </g>
    <g role="img" aria-label="Exterior of the company's blue-roofed office building with lawn">
      <polygon points="270,539 451,539 435,692 253,692" fill="url(#building)"/>
    </g>
    <g role="img" aria-label="Rolls of coiled sheet steel in a warehouse">
      <polygon points="485,539 661,539 645,692 468,692" fill="url(#coils)"/>
    </g>
  </svg>

  <section class="benefits-panel">
    <ul class="benefit-list">
      <li>Individual and Family Medical Insurance</li>
      <li>Dental Insurance</li>
      <li>Vision Insurance</li>
      <li>Short Term Disability Insurance</li>
      <li>Critical Illness and Accident Insurance</li>
      <li>No Cost Life Insurance Policy</li>
      <li>Education Cost Reimbursement</li>
    </ul>
    <ul class="benefit-list">
      <li>401K with Company Match</li>
      <li>Profit Sharing</li>
      <li>Attendance and Performance Bonuses</li>
      <li>No Cost Legal Assistance</li>
      <li>No Cost Counseling Services</li>
      <li>No Cost Tobacco Cessation Coaching</li>
      <li>No Cost College Planning Assistance</li>
    </ul>
    <ul class="benefit-list">
      <li>No Cost Work-Life Services</li>
      <li>No Cost Employee Discounts</li>
      <li>No Cost Legal Consultation</li>
      <li>No Cost Financial Consultation</li>
      <li>No Cost ID Theft Assistance</li>
      <li>No Cost Tax Consultation Assistance</li>
      <li>Up to 17 Days of Paid Time Off</li>
    </ul>
  </section>
  <h2 class="benefits-banner">BENEFITS WE OFFER AS A COMPANY</h2>

  <div class="footer-band"></div>
  <svg class="footer-graphic" viewBox="0 1050 684 150" width="684" height="150">
    <polygon points="280,1200 392,1054 684,1054 684,1060 396,1060 288,1200" fill="#d9dce1"/>
    <polygon points="288,1200 398,1060 684,1060 684,1200" fill="var(--blue)"/>
  </svg>

  <div class="contact">
    <div class="contact-row contact-phone">
      <svg width="20" height="20" viewBox="0 0 24 24" aria-hidden="true"><path fill="var(--blue)" d="M6.6 10.8a15.2 15.2 0 0 0 6.6 6.6l2.2-2.2a1 1 0 0 1 1-.25 11.4 11.4 0 0 0 3.6.57 1 1 0 0 1 1 1V20a1 1 0 0 1-1 1A17 17 0 0 1 3 4a1 1 0 0 1 1-1h3.5a1 1 0 0 1 1 1c0 1.25.2 2.45.57 3.6a1 1 0 0 1-.25 1z"/></svg>
      <span>419-555-0148</span>
    </div>
    <div class="contact-row contact-web">
      <svg width="20" height="20" viewBox="0 0 24 24" aria-hidden="true"><g fill="none" stroke="var(--blue)" stroke-width="2"><circle cx="12" cy="12" r="9.5"/><ellipse cx="12" cy="12" rx="4" ry="9.5"/><path d="M2.5 12h19M4 7h16M4 17h16"/></g></svg>
      <span>www.ironvale-steel.com</span>
    </div>
  </div>

  <div class="apply">
    <p class="apply-title">APPLY NOW!</p>
    <p class="apply-note">SEND YOUR RESUME AT</p>
    <p class="apply-email">
      <svg width="24" height="17" viewBox="0 0 24 17" aria-hidden="true"><g fill="none" stroke="#fff" stroke-width="1.6"><rect x="1" y="1" width="22" height="15"/><path d="M1 1l11 9 11-9M1 16l8-7M23 16l-8-7"/></g></svg>
      <span>jobs@ironvale-steel.com</span>
    </p>
  </div>
</main>
</body>
</html>
```